Larkspur Ridge Management - Business Cards

I need business cards. My current logo was designed by a designer at this site and I very much like and am happy with the results. I would like a business card that is trendy, unique, current yet professional. I deal with high net worth clients daily

Target Market(s)

Out of state investors looking to get into the rental market in Ohio

Industry/Entity Type

Property Management, Consulting

Contact Information for Business Card

Name, Title (Chief Financial Officer) office phone number (555) 817-3094 website address larkridgemgmt.example

Font styles to use
Sans Serif

Colors
0054AA
0677BA
7BADD7
CADEEF
E8F1F8
0094D4
00A9DD
6FCCEA
C7EBF8
E9F6FB
00AB8E
00BBA5
67D7C9
C6EFE9
E9F9F6

```html
<!DOCTYPE html>
<html lang="en">
<head>
<meta charset="utf-8">
<title>Larkspur Ridge Management – Business Cards</title>
<link rel="stylesheet" href="https://fonts.googleapis.com/css2?family=Roboto:wght@400;500;700&display=swap">
<style>
  :root {
    --navy: #22355c;
    --red: #d3242f;
    --white: #ffffff;
    --ink: #2b3a5e;
    --muted: #6b7280;
    --text: #444444;
    --backdrop: #eceef1;
  }
  * { margin: 0; padding: 0; box-sizing: border-box; }
  html, body {
    width: 1200px; height: 1200px; overflow: hidden;
    background: var(--backdrop);
    font-family: "Roboto", Arial, sans-serif;
  }
  .card {
    position: absolute; left: 150px;
    width: 900px; height: 514px;
    border-radius: 6px; overflow: hidden;
    box-shadow: 0 12px 30px rgba(20, 30, 50, 0.18);
  }
  .card--front { top: 50px; background: var(--navy); }
  .card--back { top: 636px; background: var(--white); }

  .front-brand {
    position: absolute; left: 0; right: 0; top: 190px;
    display: flex; align-items: center; justify-content: center; gap: 18px;
    color: var(--white); font-size: 38px; font-weight: 700; letter-spacing: 1px;
  }
  .brand-mark { width: 26px; height: 26px; background: var(--red); }
  .front-url {
    position: absolute; left: 0; right: 0; top: 390px; text-align: center;
    color: var(--white); font-size: 20px; letter-spacing: 6px;
  }

  .back-shape { position: absolute; inset: 0; }
  .back-brand {
    position: absolute; left: 60px; top: 150px; width: 280px;
    color: var(--navy); font-size: 34px; font-weight: 700; line-height: 1.2;
  }
  .back-divider {
    position: absolute; left: 380px; top: 60px; width: 3px; height: 230px;
    background: var(--red);
  }
  .contact { position: absolute; left: 420px; top: 70px; color: var(--ink); }
  .contact__name { font-size: 42px; font-weight: 500; color: var(--navy); }
  .contact__title { font-size: 17px; color: var(--muted); margin-top: 4px; }
  .contact__list { list-style: none; margin-top: 26px; }
  .contact__item {
    display: flex; align-items: center; gap: 14px;
    font-size: 21px; color: var(--text); margin-bottom: 12px;
    white-space: nowrap;
  }
  .contact__icon { width: 20px; height: 20px; flex: none; }
</style>
</head>
<body>
  <section class="card card--front" aria-label="Business card front">
    <div class="front-brand"><span class="brand-mark"></span>Larkspur Ridge Management</div>
    <div class="front-url">www.larkridgemgmt.example</div>
  </section>

  <section class="card card--back" aria-label="Business card back">
    <svg class="back-shape" width="900" height="514" viewBox="0 0 900 514" aria-hidden="true">
      <polygon points="80,514 778,430 892,0 900,0 900,514" fill="var(--navy)"/>
      <polyline points="50,514 764,424 880,0" fill="none" stroke="var(--white)" stroke-width="10"/>
      <polyline points="40,503 754,412 868,0" fill="none" stroke="var(--red)" stroke-width="5"/>
    </svg>
    <div class="back-brand">Larkspur Ridge Management</div>
    <div class="back-divider"></div>
    <div class="contact">
      <div class="contact__name">Jhon Doe</div>
      <div class="contact__title">Chief Financial Officer</div>
      <ul class="contact__list">
        <li class="contact__item">
          <svg class="contact__icon" viewBox="0 0 24 24" aria-hidden="true"><path fill="var(--red)" d="M6.6 10.8a15 15 0 0 0 6.6 6.6l2.2-2.2a1 1 0 0 1 1-.25 11.4 11.4 0 0 0 3.6.57 1 1 0 0 1 1 1V20a1 1 0 0 1-1 1A17 17 0 0 1 3 4a1 1 0 0 1 1-1h3.5a1 1 0 0 1 1 1c0 1.25.2 2.45.57 3.57a1 1 0 0 1-.25 1z"/></svg>
          (555) 817-3094
        </li>
        <li class="contact__item">
          <svg class="contact__icon" viewBox="0 0 24 24" aria-hidden="true"><g fill="none" stroke="var(--red)" stroke-width="2"><circle cx="12" cy="12" r="9"/><ellipse cx="12" cy="12" rx="4" ry="9"/><line x1="3" y1="12" x2="21" y2="12"/></g></svg>
          www.larkridgemgmt.example
        </li>
      </ul>
    </div>
  </section>
</body>
</html>
```